Dental Specialist Needs a Business Card

We are a state of the art dental specialty office and need a business card that looks modern but professional.
I have provided our logo design in both vertical and horizontal. We use the design on letterhead in the vertical format but provided both forms for you. Thanks

Please add the address, phone and fax numbers I listed to all designs and please leave a space for website and for my employee name on each design. Thanks 2847 Halloway Avenue, Suite K East Marlow, NY 14391 Phone (716)382-9157 Fax:(716)382-9150 My name is Miles R.Dunford,D.D.S. If you want to show it with my name but the design needs to allow for the name to be switched.

Industry/Entity Type

Business

```html
<!DOCTYPE html>
<html lang="en">
<head>
<meta charset="utf-8">
<title>Keystone Endodontics P.C. – Business Card</title>
<link rel="stylesheet" href="https://fonts.googleapis.com/css2?family=Open+Sans:wght@400&display=swap">
<style>
  :root {
    --card-bg: #ffffff;
    --ink: #1a1a1a;
    --name-blue: #5bc5f2;
    --contact-green: #8ee02a;
    --mark-blue: #5bc5f2;
  }
  html, body {
    margin: 0;
    padding: 0;
    width: 1200px;
    height: 741px;
    overflow: hidden;
    background: var(--card-bg);
  }
  .card {
    position: relative;
    width: 1200px;
    height: 741px;
    background: var(--card-bg);
    font-family: "Open Sans", Arial, sans-serif;
    overflow: hidden;
  }
  .brand-dot {
    position: absolute;
    left: 0;
    top: 0;
  }
  .brand-divider {
    position: absolute;
    left: 484px;
    top: 82px;
    width: 2px;
    height: 250px;
    background: var(--ink);
  }
  .brand-name {
    position: absolute;
    left: 512px;
    top: 140px;
    margin: 0;
    color: var(--ink);
    font-weight: 400;
  }
  .brand-name .brand-main {
    display: block;
    font-size: 80px;
    line-height: 1;
    letter-spacing: 1px;
  }
  .brand-name .brand-sub {
    display: block;
    margin-top: 18px;
    margin-left: 70px;
    font-size: 31px;
    line-height: 1;
    letter-spacing: 6px;
  }
  .doctor-name {
    position: absolute;
    left: 224px;
    top: 366px;
    margin: 0;
    font-size: 58px;
    font-weight: 400;
    line-height: 1;
    color: var(--name-blue);
    letter-spacing: 0.5px;
  }
  .contact {
    position: absolute;
    left: 226px;
    top: 452px;
    margin: 0;
    font-style: normal;
    font-size: 31px;
    line-height: 47px;
    color: var(--contact-green);
    letter-spacing: 0.5px;
  }
  .contact span { display: block; }
</style>
</head>
<body>
  <div class="card">
    <svg class="brand-dot" width="1200" height="741" viewBox="0 0 1200 741" aria-hidden="true">
      <circle cx="336" cy="192" r="100" fill="var(--mark-blue)"/>
    </svg>
    <div class="brand-divider"></div>
    <h1 class="brand-name">
      <span class="brand-main">KEYSTONE</span>
      <span class="brand-sub">Endodontics P.C.</span>
    </h1>
    <h2 class="doctor-name">Miles R. Dunford D.D.S.</h2>
    <address class="contact">
      <span>2847 Halloway Avenue, Suite K</span>
      <span>East Marlow, NY 14391</span>
      <span>Ph:(716)382-9157</span>
      <span>Fax: (716)382-9150</span>
    </address>
  </div>
</body>
</html>
```